Marlowvex Website Concept

We would like a one page website. Please refer to the attached files for more information.

Please reference file attachment version 1.1.

```html
<!DOCTYPE html>
<html lang="en">
<head>
<meta charset="utf-8">
<title>Marlowvex Security</title>
<link href="https://fonts.googleapis.com/css2?family=Open+Sans:ital,wght@0,400;0,600;0,700;1,400&display=swap" rel="stylesheet">
<style>
:root{
  --backdrop:#61a0d3;
  --page:#ffffff;
  --ink:#1f1f1f;
  --navy:#1d3550;
  --muted:#9a9a9a;
  --nav:#777777;
  --accent:#5b9bd5;
  --rule:#e6e6e6;
  --footer:#f5f5f5;
  --photo-dark:#5a5a5a;
  --photo-light:#b5b5b5;
}
*{box-sizing:border-box;margin:0;padding:0}
html,body{width:1200px;height:1000px;overflow:hidden}
body{background:var(--backdrop);font-family:"Open Sans",Arial,sans-serif;color:var(--ink)}
.page{position:absolute;left:171px;top:0;width:858px;height:1000px;background:var(--page)}
.abs{position:absolute}
.brand{left:16px;top:6px;display:flex;align-items:center;gap:8px}
.brand-mark{width:30px;height:30px;border-radius:50%;background:var(--navy)}
.brand-name{font-size:25px;font-weight:600;color:var(--navy);letter-spacing:1px}
.contact-line{right:16px;font-size:10.5px;font-weight:700;color:var(--navy);display:flex;align-items:center;gap:10px}
.header-rule{left:26px;right:26px;top:48px;border-top:1px solid var(--rule)}
.nav-active-bar{left:27px;top:47px;width:48px;height:2px;background:var(--navy)}
.nav{left:28px;top:53px;display:flex;font-size:10px;color:var(--nav)}
.nav a{text-decoration:none;color:inherit;position:absolute;white-space:nowrap}
.nav a.active{color:var(--accent)}
.search{left:814px;top:54px}
.hero{left:0;top:70px;width:858px;height:179px;background:linear-gradient(100deg,#6d6d6d 0%,#9c9c9c 35%,#bdbdbd 55%,#8a8a8a 75%,#2f2f2f 100%)}
.hero-title{left:6px;top:106px;font-size:18.5px;color:#fff;white-space:nowrap}
.hero-text{left:7px;top:133px;width:590px;font-size:10px;line-height:11px;color:#fff}
.btn{background:var(--accent);color:#fff;text-align:center}
.hero-btn{left:18px;top:180px;width:108px;height:18px;font-size:10px;line-height:18px;letter-spacing:.5px}
.feature{top:262px;width:205px;text-align:center}
.feature h3{font-size:10.5px;font-weight:700;margin-top:8px}
.feature p{font-size:8.5px;line-height:9px;color:var(--muted);margin:2px 20px 0}
.vrule{top:264px;height:78px;border-left:1px solid var(--rule)}
.hrule{left:26px;width:806px;border-top:1px solid var(--rule)}
.intro-title{left:0;width:830px;top:361px;text-align:center;font-size:14.5px;font-weight:600}
.intro-text{left:90px;width:650px;top:381px;text-align:center;font-size:8.5px;line-height:10px;color:var(--muted)}
.intro-btn{left:365px;top:415px;width:86px;height:16px;font-size:8px;line-height:16px;font-style:italic}
.side-title{left:26px;font-size:12px;display:flex;align-items:center;gap:12px}
.side-title-rule{left:26px;width:14px;border-top:1px solid var(--ink)}
.side-text{left:24px;width:190px;font-size:8.5px;line-height:9.5px;color:var(--muted)}
.view-all{left:24px;font-size:9px;color:var(--accent)}
.card{width:188px}
.card .photo{height:80px;background:linear-gradient(135deg,var(--photo-light),var(--photo-dark))}
.card h4{font-size:10.5px;font-weight:700;margin-top:2px;line-height:12px}
.card .date{font-size:8.5px;line-height:9px;color:#555;font-weight:600}
.card p{font-size:8.5px;line-height:9.5px;color:var(--muted)}
.card .card-rule{border-top:1px solid var(--rule);margin-top:8px}
.footer{left:0;top:797px;width:858px;height:203px;background:var(--footer);border-top:2px solid #ececec}
.map{left:23px;top:22px;width:243px;height:110px;background:linear-gradient(135deg,#8f8a6a,#6f7260 50%,#9a9277)}
.foot-title{font-size:10px;font-weight:600;color:#333}
.foot-text{left:299px;top:33px;width:245px;font-size:8.5px;line-height:9.5px;color:var(--muted)}
.tag{height:11px;background:#fff;font-size:8px;line-height:11px;color:var(--accent);padding-left:7px}
.label{left:573px;font-size:8px;font-weight:700;color:#333}
.field{left:573px;width:248px;background:#fff;border:1px solid #dcdcdc}
.submit{left:573px;top:148px;width:66px;height:14px;background:#8c8c8c;color:#fff;font-size:8px;line-height:14px;text-align:center;font-weight:600}
.foot-rule{left:23px;width:808px;top:176px;border-top:1px solid #e4e4e4}
.social{top:184px;width:13px;height:8px;background:var(--accent)}
.copyright{right:3px;top:181px;font-size:8.5px;color:var(--muted)}
</style>
</head>
<body>
<div class="page">
  <header>
    <div class="abs brand"><span class="brand-mark"></span><span class="brand-name">MARLOWVEX</span></div>
    <div class="abs contact-line" style="top:15px">
      <svg width="9" height="9" viewBox="0 0 10 10"><path d="M2 0.5 L3.8 2.8 L2.9 4 Q4.5 6.2 6 7.1 L7.2 6.2 L9.5 8 L8.3 9.5 Q3.5 8.5 0.5 1.7 Z" fill="var(--navy)"/></svg>
      <span>0000-000-000-00</span>
    </div>
    <div class="abs contact-line" style="top:26px">
      <svg width="10" height="8" viewBox="0 0 10 8"><rect width="10" height="8" rx="1" fill="var(--navy)"/><path d="M0.5 0.8 L5 4.5 L9.5 0.8" stroke="#fff" fill="none"/></svg>
      <span>hello@marlowvex.example</span>
    </div>
    <div class="abs header-rule"></div>
    <div class="abs nav-active-bar"></div>
    <nav class="abs nav">
      <a class="active" style="left:0">Home</a>
      <a style="left:68px">About MVX</a>
      <a style="left:161px">MVX Services</a>
      <a style="left:265px">Quote Request</a>
      <a style="left:383px">Careers</a>
      <a style="left:460px">Courses</a>
      <a style="left:540px">Crime Reports</a>
    </nav>
    <svg class="abs search" width="11" height="11" viewBox="0 0 11 11"><circle cx="4.5" cy="4.5" r="3.2" stroke="#333" stroke-width="1.5" fill="none"/><path d="M7 7 L10 10" stroke="#333" stroke-width="2"/></svg>
  </header>

  <section>
    <div class="abs hero" role="img" aria-label="Black and white photo of a security officer looking out over a city skyline"></div>
    <h1 class="abs hero-title" style="font-weight:400">Lorem Ipsum is simply dummy text of the printing</h1>
    <p class="abs hero-text">Lorem Ipsum is simply dummy text of the printing and typesetting industry. Lorem Ipsum has been the industry's standard dummy text ever since the 1500s, when an unknown printer took a galley of type and scrambled it to make.</p>
    <div class="abs btn hero-btn">READ MORE</div>
  </section>

  <section>
    <div class="abs feature" style="left:17px">
      <svg width="30" height="18" viewBox="0 0 30 18"><path d="M7 17 Q1 17 1 12 Q1 8 6 7.5 Q8 1 15 1.5 Q21 2 22.5 7 Q29 7 29 12 Q29 17 23 17 Z" fill="#111"/></svg>
      <h3>Lorem ipsum</h3>
      <p>Lorem ipsum dolor sit amet, consectetur adipisicing elit, sed do eiusmod tempor incidi-dunt</p>
    </div>
    <div class="abs vrule" style="left:223px"></div>
    <div class="abs feature" style="left:222px">
      <svg width="20" height="20" viewBox="0 0 20 20"><circle cx="10" cy="10" r="9" fill="#111"/><path d="M4 6 Q7 5 8 8 Q7 11 9 13 L8 17 M12 3 Q11 7 14 8 Q17 8 17 12 L14 15" stroke="#fff" stroke-width="1.4" fill="none"/></svg>
      <h3>Lorem ipsum</h3>
      <p>Lorem ipsum dolor sit amet, consectetur adipisicing elit, sed do eiusmod tempor incidi-dunt</p>
    </div>
    <div class="abs vrule" style="left:428px"></div>
    <div class="abs feature" style="left:428px">
      <svg width="26" height="18" viewBox="0 0 26 18"><path d="M13 1 L25 6 L13 11 L1 6 Z" fill="#111"/><path d="M1 9 L13 14 L25 9 M1 12.5 L13 17.5 L25 12.5" stroke="#111" stroke-width="1.8" fill="none"/></svg>
      <h3>Lorem ipsum</h3>
      <p>Lorem ipsum dolor sit amet, consectetur adipisicing elit, sed do eiusmod tempor incidi-dunt</p>
    </div>
    <div class="abs vrule" style="left:634px"></div>
    <div class="abs feature" style="left:633px">
      <svg width="22" height="20" viewBox="0 0 22 20"><path d="M2 19 L13 8" stroke="#111" stroke-width="3"/><path d="M8 1 V5 M6 3 H10 M17 2 V6 M15 4 H19 M18 10 V14 M16 12 H20 M13 4 L14 6" stroke="#111" stroke-width="1.2"/></svg>
      <h3>Lorem ipsum</h3>
      <p>Lorem ipsum dolor sit amet, consectetur adipisicing elit, sed do eiusmod tempor incidi-dunt</p>
    </div>
  </section>

  <div class="abs hrule" style="top:355px"></div>
  <section>
    <h2 class="abs intro-title">Lorem ipsum dolor sit amet</h2>
    <p class="abs intro-text">Lorem Ipsum is simply dummy text of the printing and typesetting industry. Lorem Ipsum has been the industry's standard dummy text ever since the 1500s, when an unknown printer took a galley of type and scrambled</p>
    <div class="abs btn intro-btn">Learn More</div>
  </section>
  <div class="abs hrule" style="top:443px"></div>

  <section>
    <h2 class="abs side-title" style="top:456px;font-weight:400">
      <svg width="14" height="10" viewBox="0 0 14 10"><rect y="2" width="14" height="8" rx="1" fill="#222"/><rect x="4.5" y="0" width="5" height="3" fill="none" stroke="#222"/></svg>
      Our Service</h2>
    <div class="abs side-title-rule" style="top:474px"></div>
    <p class="abs side-text" style="top:480px">Lorem Ipsum is simply dummy text of the printing and typesetting industry. Lorem Ipsum has been the industry's standard dummy text ever since the 1500s</p>
    <a class="abs view-all" style="top:535px">View All</a>

    <article class="abs card" style="left:232px;top:462px">
      <div class="photo" role="img" aria-label="Black and white photo of an officer loading equipment"></div>
      <h4>Lorem ipsum</h4>
      <p>Lorem ipsum dolor sit amet, con-sectetur adipisicing elit.</p>
      <div class="card-rule"></div>
    </article>
    <article class="abs card" style="left:437px;top:462px">
      <div class="photo" role="img" aria-label="Black and white photo of a security guard in a shirt and tie"></div>
      <h4>Lorem ipsum</h4>
      <p>Lorem ipsum dolor sit amet, con-sectetur adipisicing elit.</p>
      <div class="card-rule"></div>
    </article>
    <article class="abs card" style="left:643px;top:462px">
      <div class="photo" role="img" aria-label="Black and white photo of an armed guard holding a rifle"></div>
      <h4>Lorem ipsum</h4>
      <p>Lorem ipsum dolor sit amet, con-sectetur adipisicing elit.</p>
      <div class="card-rule"></div>
    </article>
  </section>

  <section>
    <h2 class="abs side-title" style="top:592px;font-weight:400;gap:6px">
      <svg width="11" height="10" viewBox="0 0 11 10"><rect y="1" width="11" height="9" rx="1" fill="#222"/><path d="M2 4 H9 M2 6.5 H9" stroke="#fff"/></svg>
      LATEST NEWS</h2>
    <div class="abs side-title-rule" style="top:609px"></div>
    <p class="abs side-text" style="top:615px">Lorem Ipsum is simply dummy text of the printing and typesetting industry. Lorem Ipsum has been the industry's standard dummy text ever since the 1500s</p>
    <a class="abs view-all" style="top:666px">View All</a>

    <article class="abs card" style="left:232px;top:594px">
      <div class="photo" role="img" aria-label="Black and white photo of soldiers in the field"></div>
      <h4 style="margin-top:5px">Lorem ipsum</h4>
      <div class="date">15 July 2014, 0 Comment</div>
      <p style="margin-top:4px">Lorem Ipsum is simply dummy text of the printing and typesetting industry. Lorem Ipsum has been the industry's standard dummy text ever since the 1500s, when an unknown printer took a galley of type and scrambled</p>
      <div class="card-rule"></div>
    </article>
    <article class="abs card" style="left:437px;top:594px">
      <div class="photo" role="img" aria-label="Black and white photo of a firearms training range"></div>
      <h4 style="margin-top:5px">Lorem ipsum</h4>
      <div class="date">15 July 2014, 0 Comment</div>
      <p style="margin-top:4px">Lorem Ipsum is simply dummy text of the printing and typesetting industry. Lorem Ipsum has been the industry's standard dummy text ever since the 1500s, when an unknown printer took a galley of type and scrambled</p>
      <div class="card-rule"></div>
    </article>
    <article class="abs card" style="left:643px;top:594px">
      <div class="photo" role="img" aria-label="Black and white photo of an instructor demonstrating a weapon"></div>
      <h4 style="margin-top:5px">Lorem ipsum</h4>
      <div class="date">15 July 2014, 0 Comment</div>
      <p style="margin-top:4px">Lorem Ipsum is simply dummy text of the printing and typesetting industry. Lorem Ipsum has been the industry's standard dummy text ever since the 1500s, when an unknown printer took a galley of type and scrambled</p>
      <div class="card-rule"></div>
    </article>
  </section>

  <footer class="abs footer">
    <div class="abs map" role="img" aria-label="Street map showing the office location"></div>

    <h3 class="abs foot-title" style="left:299px;top:16px">About Us</h3>
    <p class="abs foot-text">Lorem ipsum dolor sit amet, consectetur adipiscing elit. Maecenas sed diam eget risus varius blandit sit amet non magna. Cras mattis consectetur purus sit amet fermentum.</p>
    <h3 class="abs foot-title" style="left:299px;top:83px">Tag Cloud</h3>
    <div class="abs tag" style="left:299px;top:98px;width:48px">Lorem</div>
    <div class="abs tag" style="left:352px;top:98px;width:46px">amet</div>
    <div class="abs tag" style="left:403px;top:98px;width:52px">Lipsum</div>
    <div class="abs tag" style="left:463px;top:98px;width:60px">Lpipsum</div>
    <div class="abs tag" style="left:299px;top:113px;width:60px">Lipsum</div>
    <div class="abs tag" style="left:366px;top:113px;width:80px">Lpipsum</div>
    <div class="abs tag" style="left:450px;top:113px;width:44px">amet</div>
    <div class="abs tag" style="left:497px;top:113px;width:40px">amet</div>
    <div class="abs tag" style="left:299px;top:128px;width:42px">amet</div>
    <div class="abs tag" style="left:345px;top:128px;width:50px">Lorem</div>
    <div class="abs tag" style="left:398px;top:128px;width:46px">amet</div>
    <div class="abs tag" style="left:447px;top:128px;width:40px">amet</div>

    <h3 class="abs foot-title" style="left:572px;top:16px">Contact Form</h3>
    <div class="abs label" style="top:31px">Name *</div>
    <div class="abs field" style="top:43px;height:13px"></div>
    <div class="abs label" style="top:63px">Email *</div>
    <div class="abs field" style="top:75px;height:13px"></div>
    <div class="abs label" style="top:95px">Message *</div>
    <div class="abs field" style="top:108px;height:32px"></div>
    <div class="abs submit">Submit</div>

    <div class="abs foot-rule"></div>
    <div class="abs social" style="left:26px"></div>
    <div class="abs social" style="left:48px"></div>
    <div class="abs social" style="left:70px;background:#d9534f"></div>
    <div class="abs social" style="left:92px"></div>
    <div class="abs social" style="left:114px"></div>
    <div class="abs social" style="left:136px"></div>
    <div class="abs social" style="left:158px;background:#d9534f"></div>
    <div class="abs copyright">All rights reserved Marlowvex Security, LLC.</div>
  </footer>
</div>
</body>
</html>
```